New Interrior Decoration company needs new website

We need a website for our new company specialising in interior decoration to residential and commercial markets.
We supply and install decorative and printed films for office and home decoration such as feature walls.
We would like to keep the design simple and clean.

Target Market(s)

Architects and interior designaers

Industry/Entity Type

It Company

Number of Pages Required

5+ page

Font styles to use
Sans Serif

Requirements
Must have
• Home page,
• Services/products page (split into commercial and residential)
• Gallery (split into commercial and residential)
• contact form and page
Nice to have
• Very clean and minimalistic design.

```html
<!DOCTYPE html>
<html lang="en">
<head>
<meta charset="UTF-8">
<title>Lumen Line Interiors</title>
<link href="https://fonts.googleapis.com/css2?family=Open+Sans:wght@400;600;700&family=Raleway:wght@400;500&display=swap" rel="stylesheet">
<style>
:root{
  --blue:#0a5bbd;
  --ink:#333333;
  --muted:#666666;
  --white:#ffffff;
  --grey-band:#e8e8e8;
  --footer:#3a3a3a;
  --footer-bottom:#2a2a2a;
  --field:#555555;
}
*{margin:0;padding:0;box-sizing:border-box}
html,body{width:1200px;height:2381px;overflow:hidden}
body{position:relative;font-family:"Open Sans",Arial,sans-serif;color:var(--ink);background:var(--white)}
.abs{position:absolute}
.top-rule{left:0;top:0;width:1200px;height:5px;background:var(--blue)}
.brand{left:76px;top:30px;display:flex;align-items:center;gap:14px}
.brand-square{width:56px;height:56px;background:var(--blue)}
.brand-name{font-size:36px;font-weight:700;color:var(--ink);line-height:1;letter-spacing:1px}
.header-mail{left:622px;top:16px;font-size:17px;color:var(--ink);display:flex;align-items:center;gap:8px}
.header-phone{left:887px;top:0;width:235px;height:51px;background:var(--blue);color:var(--white);border-radius:0 0 6px 6px;display:flex;align-items:center;justify-content:center;gap:10px;font-size:22px;font-weight:600}
.nav{left:489px;top:66px;display:flex;font-size:20px;color:var(--ink)}
.nav a{display:block;height:46px;line-height:46px;text-decoration:none;color:inherit}
.nav .current{background:var(--blue);color:var(--white);width:102px;text-align:center}
.hero{left:0;top:133px;width:1200px;height:565px;background:linear-gradient(160deg,#d9dad6 0%,#b7b8b2 40%,#c9b79a 70%,#8f8a80 100%)}
.cta-band{left:0;top:698px;width:1200px;height:135px;background:var(--blue)}
.cta-text{left:89px;top:744px;font-size:32px;color:var(--white);letter-spacing:.5px}
.cta-button{left:925px;top:735px;width:197px;height:57px;background:var(--white);color:var(--ink);border-radius:4px;font-size:22px;font-weight:700;display:flex;align-items:center;justify-content:center}
.section-title{left:0;width:1200px;text-align:center;font-size:47px;font-weight:400;color:var(--ink);line-height:1}
.section-title span{color:var(--blue)}
.intro{left:171px;top:955px;width:858px;text-align:center;font-size:16px;line-height:25px;color:var(--muted)}
.service-photo{top:1065px;width:208px;height:140px}
.service-title{top:1060px;font-size:27px;color:var(--ink)}
.service-text{top:1098px;width:265px;font-size:16px;line-height:25px;color:var(--muted)}
.read-more{top:1182px;font-size:19px;color:var(--blue);display:flex;align-items:center;gap:6px}
.gallery-band{left:0;top:1274px;width:1200px;height:437px;background:var(--grey-band)}
.gallery-photo{top:1398px;width:233px;height:156px}
.view-all{left:525px;top:1589px;width:149px;height:52px;background:var(--blue);color:var(--white);border-radius:4px;font-size:21px;display:flex;align-items:center;justify-content:center}
.avatar{left:105px;top:1819px;width:156px;height:156px;border-radius:50%;background:radial-gradient(circle at 50% 45%,#c9c9c9,#a8a8a8)}
.quote{left:287px;top:1838px;width:770px;font-size:16px;line-height:25px;color:var(--muted)}
.client-name{left:287px;top:1943px;font-size:15px;font-weight:700;color:var(--blue)}
.slider-arrow{top:1878px}
.footer{left:0;top:2043px;width:1200px;height:285px;background:var(--footer)}
.footer-bottom{left:0;top:2328px;width:1200px;height:53px;background:var(--footer-bottom);color:#dddddd;font-size:15px;text-align:center;line-height:53px}
.footer-bottom strong{font-weight:700}
.footer-brand{left:78px;top:2085px;display:flex;align-items:center;gap:8px}
.footer-brand .brand-square{width:34px;height:34px}
.footer-brand .brand-name{color:var(--white);font-size:22px}
.footer-about{left:78px;top:2138px;width:240px;font-size:16px;line-height:25px;color:var(--white)}
.footer-heading{top:2067px;font-family:"Raleway",Arial,sans-serif;font-size:25px;color:var(--white)}
.footer-links{left:349px;top:2113px;list-style:none;font-size:19px;color:var(--white);line-height:36.5px}
.footer-links li{display:flex;align-items:center;gap:10px}
.contact-line{left:619px;display:flex;gap:10px;font-size:16px;color:var(--white);line-height:23px}
.social{top:2244px;width:48px;height:48px;border:2px solid var(--white);border-radius:4px}
.social.solid{background:var(--white)}
.field{left:889px;width:233px;height:36px;background:var(--field);color:var(--white);font-size:16px;padding-left:8px;line-height:36px;border-radius:2px}
.subscribe{left:889px;top:2221px;width:150px;height:46px;background:var(--blue);color:var(--white);font-size:20px;display:flex;align-items:center;justify-content:center;border-radius:2px}
</style>
</head>
<body>
<div class="abs top-rule"></div>

<header>
  <div class="abs brand"><div class="brand-square"></div><div class="brand-name">LUMEN LINE</div></div>
  <div class="abs header-mail">
    <svg width="20" height="16" viewBox="0 0 20 16"><rect x="1" y="1" width="18" height="14" rx="2" fill="none" stroke="#0a5bbd" stroke-width="2"/><path d="M1 2l9 7 9-7" fill="none" stroke="#0a5bbd" stroke-width="2"/></svg>
    info@lumenlineinteriors.com
  </div>
  <div class="abs header-phone">
    <svg width="24" height="24" viewBox="0 0 24 24"><path d="M6.6 10.8a15 15 0 006.6 6.6l2.2-2.2c.3-.3.7-.4 1-.2 1.1.4 2.3.6 3.6.6.6 0 1 .4 1 1V20c0 .6-.4 1-1 1C10.6 21 3 13.4 3 4c0-.6.4-1 1-1h3.5c.6 0 1 .4 1 1 0 1.3.2 2.5.6 3.6.1.3 0 .7-.2 1z" fill="#fff"/></svg>
    555 010 2040
  </div>
  <nav class="abs nav">
    <a class="current" href="#">HOME</a>
    <a href="#" style="margin-left:25px">ABOUT</a>
    <a href="#" style="margin-left:45px">SERVICES</a>
    <a href="#" style="margin-left:60px">GALLERY</a>
    <a href="#" style="margin-left:58px">CONTACT</a>
  </nav>
</header>

<div class="abs hero" role="img" aria-label="Modern concrete interior with a long curved wooden desk and white lamps"></div>

<section>
  <div class="abs cta-band"></div>
  <div class="abs cta-text">LOREM IPSUM IS DUMMY TEXT OF THE PRINTING.</div>
  <div class="abs cta-button">CONTACT US</div>
</section>

<section>
  <h1 class="abs section-title" style="top:890px">WELCOME TO <span>LUMEN LINE INTERIORS</span></h1>
  <p class="abs intro">Lorem Ipsum is simply dummy text of the printing and typesetting industry. Lorem Ipsum has been the industry's standard dummy text ever since the 1500s, when an unknown printer took a galley of type and scrambled it to make a type specimen book.</p>

  <div class="abs service-photo" style="left:78px;background:linear-gradient(135deg,#6b6f70,#c9c6bd 60,#8b8a86);background:linear-gradient(135deg,#5f6466,#bdb9ae 60%,#7d7b76)" role="img" aria-label="Residential room with grey feature wall and pendant lamps"></div>
  <h2 class="abs service-title" style="left:303px;font-weight:400">Residential Interiors</h2>
  <p class="abs service-text" style="left:303px">Lorem Ipsum is simply dummy text of the printing and typesetting industry Lorem Ipsum...</p>
  <div class="abs read-more" style="left:304px">READ MORE <svg width="14" height="14" viewBox="0 0 14 14"><path d="M2 2l5 5-5 5M7 2l5 5-5 5" fill="none" stroke="#0a5bbd" stroke-width="2"/></svg></div>

  <div class="abs service-photo" style="left:628px;background:linear-gradient(135deg,#e6e4df,#cfcac2 55%,#b9a99a)" role="img" aria-label="Commercial wall with printed decorative film of coloured circles"></div>
  <h2 class="abs service-title" style="left:855px;font-weight:400">Commercial Interiors</h2>
  <p class="abs service-text" style="left:855px">Lorem Ipsum is simply dummy text of the printing and typesetting industry Lorem Ipsum...</p>
  <div class="abs read-more" style="left:856px">READ MORE <svg width="14" height="14" viewBox="0 0 14 14"><path d="M2 2l5 5-5 5M7 2l5 5-5 5" fill="none" stroke="#0a5bbd" stroke-width="2"/></svg></div>
</section>

<section>
  <div class="abs gallery-band"></div>
  <h2 class="abs section-title" style="top:1332px;font-weight:400">LATEST <span>GALLERY</span></h2>
  <div class="abs gallery-photo" style="left:78px;background:linear-gradient(135deg,#3a2c22,#7a6a5a 50%,#2a211b)" role="img" aria-label="Dark living room with textured wall and vases"></div>
  <div class="abs gallery-photo" style="left:348px;background:linear-gradient(135deg,#3b1a12,#7a3a25 50%,#c9c4c8)" role="img" aria-label="Lounge chair and lamp in front of a rust wall"></div>
  <div class="abs gallery-photo" style="left:619px;background:linear-gradient(135deg,#9aa096,#c3c7bf 50%,#6f7a70)" role="img" aria-label="Corridor with stone-effect wall film"></div>
  <div class="abs gallery-photo" style="left:889px;background:linear-gradient(135deg,#8a3b2a,#b0553f 45%,#bfbdb6)" role="img" aria-label="Room with brick-effect feature wall and black sofa"></div>
  <div class="abs view-all">VIEW ALL</div>
</section>

<section>
  <h2 class="abs section-title" style="top:1763px;font-weight:400">WHAT OUR <span>CLIENT SAY</span></h2>
  <svg class="abs slider-arrow" style="left:46px" width="16" height="38" viewBox="0 0 16 38"><path d="M14 2L3 19l11 17" fill="none" stroke="#0a5bbd" stroke-width="2"/></svg>
  <div class="abs avatar" role="img" aria-label="Portrait of a client"></div>
  <p class="abs quote">Lorem Ipsum is simply dummy text of the printing and typesetting industry. Lorem Ipsum has been the industry's standard dummy text ever since the 1500s, when an unknown printer took a galley of type and scrambled it to make a type specimen book.</p>
  <div class="abs client-name">- CLIENT NAME</div>
  <svg class="abs slider-arrow" style="left:1131px" width="16" height="38" viewBox="0 0 16 38"><path d="M2 2l11 17L2 36" fill="none" stroke="#0a5bbd" stroke-width="2"/></svg>
</section>

<footer>
  <div class="abs footer"></div>
  <div class="abs footer-brand"><div class="brand-square"></div><div class="brand-name">LUMEN LINE</div></div>
  <p class="abs footer-about">Lorem Ipsum is simply dummy text of the printing and typesetting industry. Lorem Ipsum has been the industry's standard dummy text ever since the 1500.</p>

  <h3 class="abs footer-heading" style="left:349px;font-weight:400">Useful Links</h3>
  <ul class="abs footer-links">
    <li><svg width="18" height="10" viewBox="0 0 18 10"><path d="M0 5h16M12 1l4 4-4 4" fill="none" stroke="#fff" stroke-width="2"/></svg>Home</li>
    <li><svg width="18" height="10" viewBox="0 0 18 10"><path d="M0 5h16M12 1l4 4-4 4" fill="none" stroke="#fff" stroke-width="2"/></svg>About</li>
    <li><svg width="18" height="10" viewBox="0 0 18 10"><path d="M0 5h16M12 1l4 4-4 4" fill="none" stroke="#fff" stroke-width="2"/></svg>Services</li>
    <li><svg width="18" height="10" viewBox="0 0 18 10"><path d="M0 5h16M12 1l4 4-4 4" fill="none" stroke="#fff" stroke-width="2"/></svg>Gallery</li>
    <li><svg width="18" height="10" viewBox="0 0 18 10"><path d="M0 5h16M12 1l4 4-4 4" fill="none" stroke="#fff" stroke-width="2"/></svg>Contact</li>
  </ul>

  <h3 class="abs footer-heading" style="left:619px;font-weight:400">Get In Touch</h3>
  <div class="abs contact-line" style="top:2108px">
    <svg width="16" height="22" viewBox="0 0 16 22" style="flex:none;margin-top:2px"><path d="M8 0a8 8 0 00-8 8c0 6 8 14 8 14s8-8 8-14a8 8 0 00-8-8z" fill="#fff"/><circle cx="8" cy="8" r="3" fill="#3a3a3a"/></svg>
    <span style="width:220px">Lorem Ipsum is dummy text of the printing.</span>
  </div>
  <div class="abs contact-line" style="top:2166px;font-weight:700">
    <svg width="18" height="18" viewBox="0 0 24 24"><path d="M6.6 10.8a15 15 0 006.6 6.6l2.2-2.2c.3-.3.7-.4 1-.2 1.1.4 2.3.6 3.6.6.6 0 1 .4 1 1V20c0 .6-.4 1-1 1C10.6 21 3 13.4 3 4c0-.6.4-1 1-1h3.5c.6 0 1 .4 1 1 0 1.3.2 2.5.6 3.6.1.3 0 .7-.2 1z" fill="#fff"/></svg>
    555 010 2040
  </div>
  <div class="abs contact-line" style="top:2206px">
    <svg width="20" height="16" viewBox="0 0 20 16" style="margin-top:4px"><rect x="1" y="1" width="18" height="14" rx="2" fill="none" stroke="#fff" stroke-width="2"/><path d="M1 2l9 7 9-7" fill="none" stroke="#fff" stroke-width="2"/></svg>
    info@lumenlineinteriors.com
  </div>
  <div class="abs social solid" style="left:619px" aria-label="Social profile"></div>
  <div class="abs social" style="left:692px" aria-label="Social profile"></div>
  <div class="abs social" style="left:765px" aria-label="Social profile"></div>

  <h3 class="abs footer-heading" style="left:889px;font-weight:400">Newsletter</h3>
  <div class="abs field" style="top:2117px">Enter Name</div>
  <div class="abs field" style="top:2169px">Enter Email</div>
  <div class="abs subscribe">SUBSCRIBE</div>

  <div class="abs footer-bottom">© <strong>LUMEN LINE INTERIORS</strong> - 2016. All Rights Reserved.</div>
</footer>
</body>
</html>
```